Bright Kettle Crafts- Retailer

Need to describe what Bright Kettle Crafts is, what products we carry with photos and descriptions, as well as pricing for each. shopping cart, purchase items by way of Paloo and CoinDrift

Industry/Entity Type

Hobby / Entertainment

Coding

Coded - Design and coding required

Number of Pages Required

5+ page

Font styles to use
Sans Serif

Colors
0054AA
0677BA
7BADD7
CADEEF
E8F1F8
F0912C
F2A743
F7CA91
FBE8D2
FDF5EE
EE7325
F08F49
F5BC92
FAE3D3
FDF4ED

Requirements
Must have
• Product pages, shopping cart, checkout
Nice to have
• Video/gif, of working train or slot car tracks
Should not have
• Cartoon characters or images

```html
<!DOCTYPE html>
<html lang="en">
<head>
<meta charset="utf-8">
<title>Your Cart · Bright Kettle Crafts</title>
<link rel="stylesheet" href="https://fonts.googleapis.com/css2?family=Inter:ital,wght@0,400;0,500;0,600;0,700;0,800;1,400&display=swap">
<style>
:root{
  --bg-page:#0d1b30;
  --bg-header:#08131f;
  --bg-footer:#07101c;
  --bg-card:#12223b;
  --border:#1f3352;
  --text:#ffffff;
  --text-muted:#9fb6d4;
  --link:#7badd7;
  --nav:#a9c4e0;
  --orange:#f5a623;
  --blue:#2b7fd4;
  --green:#22c55e;
  --thumb:#0b1240;
  --qty-btn:#22385a;
}
*{box-sizing:border-box;margin:0;padding:0}
html,body{width:1200px;height:799px;overflow:hidden}
body{background:var(--bg-page);color:var(--text);font-family:"Inter",sans-serif;position:relative}
a{color:inherit;text-decoration:none}

.site-header{height:56px;background:var(--bg-header);border-bottom:1px solid var(--border);display:flex;align-items:center;justify-content:space-between;padding:0 73px 0 75px}
.brand{display:flex;align-items:center;gap:8px;font-weight:800;font-size:13px;letter-spacing:.08em;color:var(--text);text-transform:uppercase}
.brand-dot{width:22px;height:22px;border-radius:50%;background:var(--orange);flex:none}
.main-nav{display:flex;align-items:center;gap:18px}
.main-nav a{font-size:13px;font-weight:600;letter-spacing:.06em;color:var(--nav)}
.cart-button{display:flex;align-items:center;gap:7px;background:var(--blue);color:#fff !important;padding:7px 14px;border-radius:5px;font-size:13px;letter-spacing:0 !important;font-weight:700 !important}
.cart-count{width:15px;height:15px;border-radius:50%;background:var(--orange);font-size:9px;display:flex;align-items:center;justify-content:center;color:#fff}

.cart-page{width:667px;margin:0 auto;padding-top:56px}
.page-title{font-size:27px;font-weight:700;letter-spacing:-.02em;line-height:1}
.cart-item{margin-top:28px;height:68px;background:var(--bg-card);border:1px solid var(--border);border-radius:8px;display:flex;align-items:center;padding:0 14px}
.item-thumb{width:42px;height:42px;border-radius:6px;background:linear-gradient(135deg,#0b1240,#1a1d55);flex:none}
.item-info{margin-left:12px;flex:1}
.item-name{font-size:12.5px;font-weight:700;letter-spacing:-.02em}
.item-meta{font-size:9.5px;color:var(--link);margin-top:3px}
.qty{display:flex;align-items:center;gap:14px}
.qty-btn{width:25px;height:24px;border-radius:4px;background:var(--qty-btn);display:flex;align-items:center;justify-content:center;font-weight:800;font-size:14px}
.qty-value{font-size:14px;font-weight:600;width:6px;text-align:center}
.item-price{margin-left:22px;color:var(--orange);font-weight:700;font-size:15px}
.remove{margin-left:16px;width:12px;height:12px}

.summary{margin-top:10px;background:var(--bg-card);border:1px solid var(--border);border-radius:8px;padding:20px}
.summary-row{display:flex;justify-content:space-between;font-size:13px;color:var(--text-muted);line-height:22px}
.summary-row strong{color:var(--text);font-weight:700}
.summary-row .note{color:var(--green);font-weight:600;font-size:12px}
.summary-total{display:flex;justify-content:space-between;align-items:center;border-top:1px solid var(--border);margin-top:5px;padding-top:10px;font-weight:700;font-size:16px}
.summary-total .amount{color:var(--orange);font-size:21px}
.checkout-button{margin-top:24px;display:block;height:41px;border-radius:5px;background:var(--orange);color:#fff;font-weight:700;font-size:14px;text-align:center;line-height:41px}

.site-footer{position:absolute;left:0;top:590px;width:1200px;height:209px;background:var(--bg-footer);border-top:1px solid var(--border)}
.footer-grid{width:966px;margin:0 auto;padding-top:37px;display:grid;grid-template-columns:248px 248px 248px 222px;height:163px}
.footer-brand .brand{font-size:12px}
.footer-brand .brand-dot{width:20px;height:20px}
.tagline{margin-top:15px;font-size:10.5px;font-style:italic;color:var(--link)}
.footer-col h3{font-size:12.5px;font-weight:700;margin-top:4px;margin-bottom:6px}
.footer-col li{list-style:none;font-size:11.5px;color:var(--link);line-height:19.5px}
.contact li{display:flex;align-items:center;gap:7px;line-height:20.5px}
.contact svg{width:10px;height:10px;flex:none}
.footer-bottom{width:966px;margin:0 auto;border-top:1px solid var(--border);display:flex;justify-content:space-between;padding-top:17px;font-size:10.5px;color:var(--text-muted)}
.footer-bottom .made{color:var(--link)}
</style>
</head>
<body>
<header class="site-header">
  <a class="brand" href="#"><span class="brand-dot"></span>Bright Kettle Crafts</a>
  <nav class="main-nav">
    <a href="#">HOME</a><a href="#">SHOP</a><a href="#">ABOUT</a><a href="#">CONTACT</a>
    <a class="cart-button" href="#">
      <svg width="15" height="15" viewBox="0 0 24 24" fill="none" stroke="#fff" stroke-width="2"><path d="M6 7h12l-1 13H7z"/><path d="M9 7a3 3 0 0 1 6 0"/></svg>
      <span class="cart-count">1</span>Cart
    </a>
  </nav>
</header>

<main class="cart-page">
  <h1 class="page-title">Your Cart</h1>
  <div class="cart-item">
    <div class="item-thumb" role="img" aria-label="Product photo of the classic racing slot car"></div>
    <div class="item-info">
      <div class="item-name">Classic Racing Slot Car Set</div>
      <div class="item-meta">1/32 Scale · SC-2001</div>
    </div>
    <div class="qty">
      <span class="qty-btn">−</span><span class="qty-value">1</span><span class="qty-btn">+</span>
    </div>
    <div class="item-price">$59.95</div>
    <svg class="remove" viewBox="0 0 12 12" stroke="#5d7594" stroke-width="1.3"><path d="M1 1l10 10M11 1L1 11"/></svg>
  </div>

  <section class="summary">
    <div class="summary-row"><span>Subtotal</span><strong>$59.95</strong></div>
    <div class="summary-row"><span>Shipping</span><span class="note">Calculated at checkout</span></div>
    <div class="summary-total"><span>Total</span><span class="amount">$59.95</span></div>
    <a class="checkout-button" href="#">Proceed to Checkout →</a>
  </section>
</main>

<footer class="site-footer">
  <div class="footer-grid">
    <div class="footer-brand">
      <a class="brand" href="#"><span class="brand-dot"></span>Bright Kettle Crafts</a>
      <p class="tagline">"Hands On Hobbies. One Build At A Time."</p>
    </div>
    <div class="footer-col">
      <h3>Shop</h3>
      <ul><li>Die-Cast Trucks</li><li>Model Trains</li><li>Slot Cars</li><li>Accessories</li></ul>
    </div>
    <div class="footer-col">
      <h3>Company</h3>
      <ul><li>About Us</li><li>Contact</li><li>Cart</li></ul>
    </div>
    <div class="footer-col contact">
      <h3>Get In Touch</h3>
      <ul>
        <li><svg viewBox="0 0 10 10"><path d="M2 1l2 2-1 1.2a6 6 0 0 0 2.8 2.8L7 6l2 2-1.2 1.2C4.5 9 1 5.5.8 2.2z" fill="#e0463a"/></svg>555-014-2290</li>
        <li><svg viewBox="0 0 10 10"><rect x="0.5" y="2" width="9" height="6.5" fill="#e8eef6"/><path d="M.5 2l4.5 3.5L9.5 2" stroke="#8aa0bb" fill="none" stroke-width=".8"/></svg>hello@brightkettlecrafts.com</li>
        <li><svg viewBox="0 0 10 10" fill="none" stroke="#4aa3e8" stroke-width=".9"><circle cx="5" cy="5" r="4.3" fill="#1f6fb5"/><path d="M.7 5h8.6M5 .7c2 2.5 2 6.1 0 8.6M5 .7c-2 2.5-2 6.1 0 8.6"/></svg>www.brightkettlecrafts.com</li>
      </ul>
    </div>
  </div>
  <div class="footer-bottom">
    <span>© 2025 Bright Kettle Crafts · Dana Whitfield</span>
    <span class="made">Made for collectors &amp; hobbyists everywhere</span>
  </div>
</footer>
</body>
</html>
```